Skincare Label Design Completion

I am starting up a skincare business and need the graphic design completed.

A previous designer started the project but was not able to finish. The logo, BC, letterhead, With Comp & gift voucher is complete. The BC, Letterhead, WC & GV need change of contact details. The BC needs a bit of wording transferred from front to back to look 'cleaner'. There are 15 product labels which need finishing; one is 95% complete, two are 80% complete, 11 have the groundwork done, one is not started at all. Pantone has been used, this may need changing to CMYK as printers prefer this.

PRODUCT NAMES, PACKAGING AND SPECS: All attached.

LOGO SYMBOL: Is a simple wheat image. The .ai file it can be 'pulled' out of is attached.

FRENCH TRANSLATION: The French translations of product names are to feature within the label. (Please see attached pdf's; look for the colour "stripe".)

PRODUCT DIFFERENTIATION: A unique colour is to be introduced to each product label that corresponds to the botanical ingredients found within. Ie: a light green to match Aloe Vera. That secondary colour is to feature (minimally) within that label. In the attached pdf's it's been placed as a contrasting colour stripe. Other ideas welcome. :)

BOTANICAL IMAGES: THIS IS NON-ESSENTIAL - A simple botanical image could feature on each label to correspond to the product name, instead of the colour stripe. Ie: A rosehip and rose flower on the Rosehip, Lavender and Jojoba Facial Cleanser.

COLOUR MATCHING: Each of the "secondary" colours (please see Product Differentiation) need to match each other as well as the logo colours. Some of the products are designed as combo's; ie, cleanser and moisturiser combo's. The colours for these combo's need to work together. The previous designer did a pdf of suggested secondary colours (attached), however these are mostly not in sync with the businesses' approach of earthy/simple/easy to look at/purity. A friend did a pdf of earthy green secondary colours (pdf attached entitled "Mon_Ciel_Clair_FC") and did a few creative suggestions for the label. The font, colours and design he used in the TOP LEFT label is the one I prefer but please use your creative license should you feel a different font would look better.

- LABEL INFO -
95% COMPLETED LABEL: See pdf "Mon_Ciel_Clair_FC"; top left label, product "Aloe & Lemon Myrtle Facial Cleanser". This needs the light writing at the top changed to Pantone Black 5C, and a colour decided upon for the stripe (see below for more info). The product info needs to be checked for accuracy against the word doc I've provided. (Some info has changed.) Note: All of the cleansers, moisturisers, the spray mist and the hand cream use this exact same label as above, only with a different colour stripe for differentiation and wording / title changed.

80% COMPLETED LABELS: See pdf "Mon Ciel Clair_label_ v4-1":
1) "Clarifying Macadamia & Green Clay Facial Masque" needs a different colour stripe selected/inserted, the light writing above the logo needs changed to Pantone Black 5C, the font needs to be made the same as the above label "Aloe & Lemon Myrtle Facial Cleanser", and the product info updated as per the product info word doc attached.
2) "Cocoa Butter & Apricot Body Cream" need a different colour stripe selected/inserted, the font changed to the same as "Aloe & Lemon Myrtle Facial Cleanser" label, and the product info updated as per the word doc attached. The other labels on that pdf can be dismissed.

INCOMPLETE LABELS: As noted above, the "Aloe & Lemon Myrtle" cleanser label is exactly the same for 7 other products (cleansers, moisturisers, spray mist and hand cream). The "Mon_Ciel_Clair_FC" can be used as the basis for these. Each one needs a different colour stripe for differentiation chosen and inserted, and the light wording above the logo changed to Black 5C.

The products "Sandalwood & Shea Butter Facial Exfoliating Cream", "Jojoba, Ylang Ylang & Vanilla Facial Exfoliant" and "Sweet Orange & Lavender Hand & Foot Scrub" all use exactly the same labels (one for jar, one for lid) as the Clarifying Macadamia & Green Clay masque. So you should be able to replicate this label for the other products. Each of these need the light writing above the logo changed to Black 5C and the colour stripes selected/inserted.

In the pdf "Mon Ciel Clair_label_ v4-1" the the 250mL bottle label has been completed. However that particular product was deleted. So using that label you can "pull out" the discontinued label wording and colour stripe, and replace it with the "Rosehip Body Lotion" label info. This also needs the light writing above the logo to be replaced with Pantone Black 5C, the colour stripe decided upon/inserted and the font to match with the above.

Only the lip balm has absolutely no work done on it. This will be just one small rectangular label.

Please note: this is not a re-branding so please stay true to the logo colours of Pantone 2717C, 4685C and Black 5C for the majority of the label. Secondary colour use is fine to match the botanicals.

Thank you so much in advance for your designs! :)

Maren.

Target Market(s)

Women aged 16 - 65+
Environmentally aware
Natural over chemical
Will spend a higher amount for a quality product
Women who want the best

Industry/Entity Type

Graphic Design

Font styles to use
Other font styles liked:
• Attached pdf "Mon_Ciel_Clair_FC" - top left label

Requirements
Must have
• Simple, clean lines, purity, natural / earthy colours.
• Secondary colours carefully chosen to reflect the botanical ingredients and to match the logo colours and each other.
• French translations on labels.
• LABELS MUST STAY WITH COLOURS MENTIONED IN BRIEF: PANTONE 2717C, 4685C, BLACK 5C - This is not a re-branding so please don't stray from using these colours for the majority of the label. (For secondary colour use to match botanicals, please use your creative license.)
Nice to have
• Botanical image on each label - non-essential
Should not have
• Nothing modern, harsh, stark or intense

```html
<!DOCTYPE html>
<html lang="en">
<head>
<meta charset="utf-8">
<title>Mon Ciel Clair – Coconut &amp; Lemon Myrtle Moisturiser Label</title>
<link rel="stylesheet" href="https://fonts.googleapis.com/css2?family=Didact+Gothic&family=Great+Vibes&family=Open+Sans:ital,wdth,wght@0,75,300;0,75,700;0,100,400;0,100,600;1,75,300;1,75,700;1,100,400&display=swap">
<style>
  :root{
    --sky:#a8c4e6;
    --sky-line:#b7d0ee;
    --ink:#3a2a26;
    --white:#ffffff;
    --rust:#bd5f39;
    --amber:#d08a3a;
    --olive:#6a7231;
    --walnut:#7d5a3b;
    --cocoa:#4a3427;
    --sage:#9c9b5a;
    --straw:#ecdb93;
    --pearl:#f1f1f1;
    --board-top:#5c5c5c;
    --board-mid:#8c8c8c;
    --board-dark:#1c1c1c;
  }
  *{margin:0;padding:0;box-sizing:border-box}
  html,body{width:1200px;height:1000px;overflow:hidden}
  body{
    position:relative;
    font-family:"Open Sans",sans-serif;
    background:linear-gradient(180deg,var(--board-top) 0%,var(--board-mid) 52%,var(--board-dark) 58%,#5a5a5a 70%,#d8d8d8 86%,#ffffff 100%);
  }
  .label-sheet{
    position:absolute;left:32px;top:30px;width:746px;height:938px;
    background:var(--sky);border-radius:12px;
    box-shadow:6px 8px 14px rgba(0,0,0,.45);
    overflow:hidden;color:var(--white);
  }
  .fine{
    font-family:"Open Sans",sans-serif;font-stretch:75%;font-weight:300;
    font-size:8.6px;line-height:10.9px;
  }
  .fine h4{font-weight:700;font-size:8.6px}
  .info-block{position:absolute;left:18px;width:170px;text-align:justify}
  .block-description{top:25px}
  .block-ingredients{top:167px}
  .block-free{top:278px}
  .block-apply{top:321px;text-align:left}
  .info-right{position:absolute;left:560px;width:180px}
  .info-right strong{font-weight:700}
  .info-right em{font-style:italic}
  .warning{top:25px}
  .cruelty{top:72px}
  .storage{top:113px}
  .contact{position:absolute;left:560px;top:296px;width:190px}
  .contact strong{font-weight:700}
  .centre-panel{
    position:absolute;left:208px;top:0;width:330px;height:400px;
    background:repeating-linear-gradient(180deg,transparent 0 4px,var(--sky-line) 4px 5px);
  }
  .ribbon{
    position:absolute;left:208px;top:25px;width:330px;height:40px;
    background:var(--rust);text-align:center;
    font-family:"Didact Gothic",sans-serif;font-size:11.5px;letter-spacing:1.2px;line-height:15px;padding-top:5px;color:#f6e3d6;
  }
  .ribbon-rule{position:absolute;left:268px;top:71px;width:210px;height:2px;background:linear-gradient(90deg,transparent,#c9d66a,transparent)}
  .brand-box{
    position:absolute;left:221px;top:86px;width:303px;height:128px;
    border:2px solid var(--white);border-radius:6px;
    display:flex;align-items:center;justify-content:center;
  }
  .brand-box::after{content:"";position:absolute;inset:4px;border:1px solid var(--white);border-radius:4px}
  .brand-name{font-family:"Didact Gothic",sans-serif;font-size:34px;color:var(--ink)}
  .product-title{
    position:absolute;left:208px;top:252px;width:330px;text-align:center;
    font-family:"Didact Gothic",sans-serif;color:var(--ink);
  }
  .product-title h1{font-weight:400;font-size:18px;letter-spacing:1px;line-height:22px}
  .product-title .skin{font-family:"Open Sans",sans-serif;font-size:10.5px;margin-top:6px}
  .product-title .organic{font-family:"Open Sans",sans-serif;font-style:italic;font-size:9px;margin-top:1px}
  .title-rule{position:absolute;left:293px;top:338px;width:160px;height:2px;background:linear-gradient(90deg,transparent,var(--rust),transparent)}
  .volume{position:absolute;left:208px;top:378px;width:330px;text-align:center;font-weight:600;font-size:11.5px;color:var(--ink)}
  .stripe{
    position:absolute;left:0;width:746px;height:41px;
    display:flex;align-items:center;
    background-image:repeating-linear-gradient(180deg,rgba(255,255,255,.08) 0 2px,transparent 2px 5px);
  }
  .stripe::before{content:"";position:absolute;left:0;right:0;top:-5px;height:2px;background:inherit}
  .stripe .icons{display:flex;gap:22px;margin-left:18px;width:190px}
  .stripe svg{width:28px;height:26px}
  .stripe .french{font-family:"Great Vibes",cursive;font-size:19px;color:var(--white);letter-spacing:.3px}
  .stripe.light .french{color:var(--ink)}
  .rust{top:400px;background-color:var(--rust)}
  .amber{top:466px;background-color:var(--amber)}
  .olive{top:532px;background-color:var(--olive)}
  .walnut{top:598px;background-color:var(--walnut)}
  .cocoa{top:664px;background-color:var(--cocoa)}
  .sage{top:730px;background-color:var(--sage)}
  .straw{top:796px;background-color:var(--straw)}
  .pearl{top:862px;background-color:var(--pearl)}
  .icon-ink{stroke:var(--ink);fill:none;stroke-width:1.4}
  .icon-fill{fill:var(--ink)}
  .note{position:absolute;left:812px;top:418px;width:210px;
    font-family:"Didact Gothic",sans-serif;font-size:22px;line-height:29px;color:var(--white);
    text-shadow:1px 1px 2px rgba(0,0,0,.4)}
  .sample-box{position:absolute;left:873px;top:770px;width:283px;height:120px;background:var(--white);
    border:2px solid #222;border-radius:6px;display:flex;align-items:center;justify-content:center}
  .sample-box::after{content:"";position:absolute;inset:4px;border:1px solid #222;border-radius:4px}
  .sample-box .brand-name{font-size:30px;color:#222}
  .spec{position:absolute;left:873px;top:908px;color:#111;font-family:"Open Sans",sans-serif}
  .spec h2{font-weight:400;font-size:22px;line-height:28px}
  .spec p{font-style:italic;font-size:14.5px}
</style>
</head>
<body>
  <section class="label-sheet">
    <div class="centre-panel"></div>

    <div class="info-block block-description fine">
      <h4>DESCRIPTION :</h4>
      <p>It is traditionally known that Coconut Oil assists in promoting skin elasticity and hydration, leaving the skin lightly moisturised, supple and less prone to blemishes.</p>
      <p>With a unique blend of Coconut Oil and the citrus properties of Lemon Myrtle, this pleasantly refreshing moisturiser provides light hydration which is quickly absorbed and leaves your complexion fresh, radiant and supple - perfect for skin prone to oiliness.</p>
    </div>
    <div class="info-block block-ingredients fine">
      <h4>INGREDIENTS :</h4>
      <p>Purified Water; Natural Vitamin E; Certified Organic Oils: Apricot, Coconut &amp; Jojoba; PEG-40 Hydrogenated Castor Oil; Aloe Vera Leaf Juice Powder; Bergamot Bergatene Free Oil; Certified Organic Oils: Lemon Myrtle &amp; Lavender; Phenoxyethanol; Caprylyl Glycol; Xanthan Gum; Carbomer; Sodium Hydroxide.</p>
    </div>
    <div class="info-block block-free fine">
      <h4>FREE OF:</h4>
      <p>Parabens, Sulfates, Propylene Glycol, DEA, Artificial Colours and Artificial Fragrances.</p>
    </div>
    <div class="info-block block-apply fine">
      <h4>TO APPLY:</h4>
      <p>After cleansing and toning, apply a small amount to your face, neck and décolletage</p>
    </div>

    <div class="ribbon">BOTANICAL FACE &amp; BODY PRODUCTS<br>HAND-MADE WITH PASSION &amp; CONSCIENCE</div>
    <div class="ribbon-rule"></div>
    <div class="brand-box"><span class="brand-name">Mon Ciel Clair</span></div>

    <div class="product-title">
      <h1>COCONUT &amp; LEMON<br>MYRTLE MOISTURISER</h1>
      <p class="skin">Especially for Normal to Oily Skin Types</p>
      <p class="organic">Containing Certified Organic Ingredients</p>
    </div>
    <div class="title-rule"></div>
    <div class="volume">125ml</div>

    <p class="info-right warning fine"><strong>Not for ingestion. In the event of a negative reaction, discontinue use and consult a medical professional.</strong></p>
    <p class="info-right cruelty fine"><em><strong>Mon Ciel Clair</strong> is Against Animal Testing – 100% Cruelty Free.</em></p>
    <p class="info-right storage fine">STORE BELOW: 21° C</p>
    <div class="contact fine">
      <strong>Mon Ciel Clair</strong><br>Address Line 1, address line 2<br>City.<br><br>
      Phone : 0391234508<br>Mobile : 0412987330<br>E - mail : maren@moncielclairorganics.com<br>www.moncielclaironline.com
    </div>

    <div class="stripe rust"><div class="icons"><svg viewBox="0 0 28 26"><path class="icon-ink" d="M4 12h20v10H4zM4 12l3-8 17 4"/><text x="8" y="20" font-size="6" class="icon-fill" font-family="sans-serif">18M</text></svg><svg viewBox="0 0 28 26"><path class="icon-fill" d="M14 2l5 8h-4l3 5-4-2-4 2 3-5h-4zM3 20l4-7 2 3 3-1-3 8H4zM25 20l-4-7-2 3-3-1 3 8h5z"/></svg></div><span class="french">Hydratant à la noix de coco et au myrte citronné</span></div>
    <div class="stripe amber"><div class="icons"><svg viewBox="0 0 28 26"><path class="icon-ink" d="M4 12h20v10H4zM4 12l3-8 17 4"/><text x="8" y="20" font-size="6" class="icon-fill" font-family="sans-serif">18M</text></svg><svg viewBox="0 0 28 26"><path class="icon-fill" d="M14 2l5 8h-4l3 5-4-2-4 2 3-5h-4zM3 20l4-7 2 3 3-1-3 8H4zM25 20l-4-7-2 3-3-1 3 8h5z"/></svg></div><span class="french">Hydratant à la noix de coco et au myrte citronné</span></div>
    <div class="stripe olive"><div class="icons"><svg viewBox="0 0 28 26"><path class="icon-ink" d="M4 12h20v10H4zM4 12l3-8 17 4"/><text x="8" y="20" font-size="6" class="icon-fill" font-family="sans-serif">18M</text></svg><svg viewBox="0 0 28 26"><path class="icon-fill" d="M14 2l5 8h-4l3 5-4-2-4 2 3-5h-4zM3 20l4-7 2 3 3-1-3 8H4zM25 20l-4-7-2 3-3-1 3 8h5z"/></svg></div><span class="french">Hydratant à la noix de coco et au myrte citronné</span></div>
    <div class="stripe walnut"><div class="icons"><svg viewBox="0 0 28 26"><path class="icon-ink" d="M4 12h20v10H4zM4 12l3-8 17 4"/><text x="8" y="20" font-size="6" class="icon-fill" font-family="sans-serif">18M</text></svg><svg viewBox="0 0 28 26"><path class="icon-fill" d="M14 2l5 8h-4l3 5-4-2-4 2 3-5h-4zM3 20l4-7 2 3 3-1-3 8H4zM25 20l-4-7-2 3-3-1 3 8h5z"/></svg></div><span class="french">Hydratant à la noix de coco et au myrte citronné</span></div>
    <div class="stripe cocoa"><div class="icons"><svg viewBox="0 0 28 26" style="opacity:.5"><path class="icon-ink" style="stroke:#bbb" d="M4 12h20v10H4zM4 12l3-8 17 4"/><text x="8" y="20" font-size="6" fill="#bbb" font-family="sans-serif">18M</text></svg><svg viewBox="0 0 28 26" style="opacity:.6"><path fill="#bbb" d="M14 2l5 8h-4l3 5-4-2-4 2 3-5h-4zM3 20l4-7 2 3 3-1-3 8H4zM25 20l-4-7-2 3-3-1 3 8h5z"/></svg></div><span class="french">Hydratant à la noix de coco et au myrte citronné</span></div>
    <div class="stripe sage"><div class="icons"><svg viewBox="0 0 28 26"><path class="icon-ink" d="M4 12h20v10H4zM4 12l3-8 17 4"/><text x="8" y="20" font-size="6" class="icon-fill" font-family="sans-serif">18M</text></svg><svg viewBox="0 0 28 26"><path class="icon-fill" d="M14 2l5 8h-4l3 5-4-2-4 2 3-5h-4zM3 20l4-7 2 3 3-1-3 8H4zM25 20l-4-7-2 3-3-1 3 8h5z"/></svg></div><span class="french">Hydratant à la noix de coco et au myrte citronné</span></div>
    <div class="stripe straw light"><div class="icons"><svg viewBox="0 0 28 26"><path class="icon-ink" d="M4 12h20v10H4zM4 12l3-8 17 4"/><text x="8" y="20" font-size="6" class="icon-fill" font-family="sans-serif">18M</text></svg><svg viewBox="0 0 28 26"><path class="icon-fill" d="M14 2l5 8h-4l3 5-4-2-4 2 3-5h-4zM3 20l4-7 2 3 3-1-3 8H4zM25 20l-4-7-2 3-3-1 3 8h5z"/></svg></div><span class="french">Hydratant à la noix de coco et au myrte citronné</span></div>
    <div class="stripe pearl light"><div class="icons"><svg viewBox="0 0 28 26"><path class="icon-ink" d="M4 12h20v10H4zM4 12l3-8 17 4"/><text x="8" y="20" font-size="6" class="icon-fill" font-family="sans-serif">18M</text></svg><svg viewBox="0 0 28 26"><path class="icon-fill" d="M14 2l5 8h-4l3 5-4-2-4 2 3-5h-4zM3 20l4-7 2 3 3-1-3 8H4zM25 20l-4-7-2 3-3-1 3 8h5z"/></svg></div><span class="french">Hydratant à la noix de coco et au myrte citronné</span></div>
  </section>

  <p class="note">Few secondary color options for labels.</p>

  <div class="sample-box"><span class="brand-name">Mon Ciel Clair</span></div>
  <div class="spec">
    <h2>Label Design</h2>
    <p>Size : 120mm(w) x 75mm(h)</p>
  </div>
</body>
</html>
```